Medical equipment business looking for professional, unique business card

We need a business card design for a durable medical equipment company. We are small but would like our cards to express that we are much bigger. We focus on braces (back, knee, wrist, etc) but also do crutches, rollators, wheelchairs- basically medical equipment that gets you going and back in Action. Our colors are blue and green and our logo has an arrow and use of a "spine". We'd like to express professionalism while being unique.

Industry/Entity Type

Medical Equipment

Contact Information for Business Card

Professional feel but unique. Memorable.

Font styles to use
Serif
Sans Serif
Other font styles liked:
• verdana

Requirements
Must have
• card holders cell#, business phone#, fax#, email, website address, business address, logo
Nice to have
• use of medical/healthcare related descriptive words, items, look
Should not have
• the wrong colors or cartoon characters.

```html
<!DOCTYPE html>
<html lang="en">
<head>
<meta charset="utf-8">
<title>Stride Medical – Business Card</title>
<link href="https://fonts.googleapis.com/css2?family=Quicksand:wght@400;500;600;700&display=swap" rel="stylesheet">
<style>
  :root {
    --navy: #0c4470;
    --navy-deep: #093a61;
    --green: #8cc63f;
    --white: #ffffff;
    --paper: #eef0f2;
  }
  * { margin: 0; padding: 0; box-sizing: border-box; }
  html, body {
    width: 1200px; height: 902px; overflow: hidden;
    background: var(--paper);
    font-family: "Quicksand", Verdana, sans-serif;
  }
  .card {
    position: absolute; left: 100px; top: 165px;
    width: 1000px; height: 572px;
    background: var(--navy);
    box-shadow: 0 18px 40px rgba(0,0,0,.18);
    overflow: hidden;
  }
  .card__band {
    position: absolute; left: 0; top: 362px;
    width: 100%; height: 142px;
    background: var(--white);
  }
  .holder {
    position: absolute; top: 50px; left: 0; width: 100%;
    display: flex; flex-direction: column; align-items: center;
    color: var(--white);
  }
  .holder__name {
    display: flex; align-items: flex-end; gap: 14px;
    margin-left: 84px;
    font-size: 34px; font-weight: 500; letter-spacing: .5px; line-height: 1.1;
  }
  .holder__name::after {
    content: ""; width: 70px; height: 2px; background: var(--green);
    margin-bottom: 8px;
  }
  .holder__role {
    display: flex; align-items: center; gap: 12px;
    margin-top: 2px; margin-left: 60px;
    font-size: 21px; font-weight: 500; line-height: 1.2;
  }
  .holder__role::before {
    content: ""; width: 90px; height: 2px; background: var(--green);
  }
  .contacts {
    position: absolute; top: 150px; left: 0; width: 100%; height: 180px;
    color: var(--white);
  }
  .contacts__divider {
    position: absolute; left: 520px; top: 4px; height: 170px;
    border-left: 5px dotted var(--green);
  }
  .contact {
    position: absolute; display: flex; align-items: center; gap: 16px;
    font-size: 21px; font-weight: 500; white-space: nowrap;
  }
  .contact--left { right: 512px; }
  .contact--right { left: 548px; }
  .contact__icon { width: 24px; height: 24px; flex: none; fill: var(--white); }
  .contact__text--address { line-height: 1.2; font-size: 19px; }
  .brand {
    position: absolute; left: 70px; top: 392px;
    display: flex; align-items: center; gap: 18px;
  }
  .brand__dot { width: 28px; height: 28px; border-radius: 50%; background: var(--green); }
  .brand__name {
    font-size: 54px; font-weight: 700; color: var(--navy); letter-spacing: .5px;
  }
  .products {
    position: absolute; left: 610px; top: 384px;
    display: grid; grid-template-columns: 165px 175px; row-gap: 28px;
    list-style: none; color: var(--navy); font-size: 25px; font-weight: 500;
  }
  .products li { display: flex; align-items: center; gap: 14px; }
  .products li::before {
    content: ""; width: 8px; height: 8px; border-radius: 50%; background: var(--green);
  }
</style>
</head>
<body>
  <section class="card" aria-label="Stride Medical business card">
    <div class="card__band"></div>

    <header class="holder">
      <div class="holder__name">Mara Ellison</div>
      <div class="holder__role">Manager</div>
    </header>

    <div class="contacts">
      <span class="contacts__divider"></span>

      <div class="contact contact--left" style="top:18px">
        <span class="contact__text">555 .014 .270</span>
        <svg class="contact__icon" viewBox="0 0 24 24" aria-hidden="true"><rect x="6" y="1" width="12" height="22" rx="2" fill="none" stroke="#fff" stroke-width="2"/><circle cx="12" cy="19" r="1.2"/></svg>
      </div>
      <div class="contact contact--left" style="top:72px">
        <span class="contact__text">mara@stridemedical.com</span>
        <svg class="contact__icon" viewBox="0 0 24 24" aria-hidden="true"><rect x="1" y="5" width="22" height="14" rx="1"/><path d="M2 6l10 7 10-7" fill="none" stroke="#0c4470" stroke-width="1.6"/></svg>
      </div>
      <div class="contact contact--left" style="top:126px">
        <span class="contact__text">www.stridemedical.com</span>
        <svg class="contact__icon" viewBox="0 0 24 24" aria-hidden="true"><g fill="none" stroke="#fff" stroke-width="2.4"><rect x="2" y="8" width="11" height="8" rx="4"/><rect x="11" y="8" width="11" height="8" rx="4"/></g></svg>
      </div>

      <div class="contact contact--right" style="top:0">
        <svg class="contact__icon" viewBox="0 0 24 24" aria-hidden="true"><path d="M6.6 10.8a15 15 0 0 0 6.6 6.6l2.2-2.2c.3-.3.7-.4 1-.2 1.1.4 2.3.6 3.6.6.6 0 1 .4 1 1V20c0 .6-.4 1-1 1A17 17 0 0 1 3 4c0-.6.4-1 1-1h3.5c.6 0 1 .4 1 1 0 1.3.2 2.5.6 3.6.1.3 0 .7-.2 1z"/></svg>
        <span class="contact__text">555 .014 .271</span>
      </div>
      <div class="contact contact--right" style="top:52px">
        <svg class="contact__icon" viewBox="0 0 24 24" aria-hidden="true"><rect x="6" y="2" width="12" height="6"/><rect x="2" y="9" width="20" height="9" rx="1.5"/><rect x="6" y="15" width="12" height="7" fill="#fff" stroke="#0c4470" stroke-width="1.5"/></svg>
        <span class="contact__text">555 .014 .272</span>
      </div>
      <div class="contact contact--right" style="top:104px">
        <svg class="contact__icon" viewBox="0 0 24 24" aria-hidden="true"><path d="M12 2L1 12h3v10h6v-6h4v6h6V12h3z"/></svg>
        <span class="contact__text contact__text--address">42 Harbour Row<br>Easton, Bristol</span>
      </div>
    </div>

    <div class="brand">
      <span class="brand__dot"></span>
      <span class="brand__name">Stride Medical</span>
    </div>

    <ul class="products">
      <li>braces</li>
      <li>rollators</li>
      <li>crutches</li>
      <li>wheelchairs</li>
    </ul>
  </section>
</body>
</html>
```